New Zealand Costume Website

Hello,

I am building a costume website for New Zealand. I have a template design in place, which I'm happy with but I require the design to be tidied up. For example, the design of banners, logo and general look and feel. I am happy with the layout of the website so it's really just the graphics/banners that need designing.

I need the design to reflect the NZ market so I'd like designs that use the Kiwi bird, which can be seen in the successful pivalo.co.nz website. The design should be fun and geared towards children.

The URL of the site is brindlehop.co.nz.

Thanks,

Oliver.

Reason: Apologies, I need to fill the site with content. Will take about 4 days. This will help u design the site.

Target Market(s)

Parents looking to buy fancy dress costumes for their children.

Requirements
Nice to have
• Ecommerce website design experience

```html
<!DOCTYPE html>
<html lang="en">
<head>
<meta charset="utf-8">
<title>Brindlehop – Return &amp; Exchange Policy</title>
<link rel="stylesheet" href="https://fonts.googleapis.com/css2?family=Arimo:wght@400;700&family=Arvo:wght@400;700&display=swap">
<style>
:root{
  --plum:#9b2d5e;
  --plum-dark:#85204f;
  --cream:#faf6ea;
  --sage:#dfe3d3;
  --ink:#222;
  --muted:#555;
  --yellow:#f7c300;
  --orange:#f39200;
  --tan:#c8a27a;
  --slate:#7d8c90;
  --box-line:#d7d9c9;
  --white:#fff;
  --alert:#e0393e;
}
*{box-sizing:border-box;margin:0;padding:0}
html,body{width:868px;height:1200px;overflow:hidden}
body{position:relative;font-family:"Arimo",Arial,sans-serif;color:var(--ink);
  background:linear-gradient(to bottom,var(--sage) 110px,#f4f5ef 300px,var(--white) 420px);}
.stripe{position:absolute;left:0;width:868px;height:5px;
  background:repeating-linear-gradient(90deg,#e94b6a 0 14px,#f6b400 14px 28px,#5aa9d6 28px 42px,#8cc63f 42px 56px,#9b2d5e 56px 70px,#f28c28 70px 84px);}
.stripe.top{top:0}.stripe.bottom{bottom:0}
.site-header{position:absolute;top:0;left:0;width:868px;height:63px;background:var(--cream)}
.brand{position:absolute;left:125px;top:18px;display:flex;align-items:center;gap:8px}
.brand-dot{width:26px;height:26px;border-radius:50%;background:var(--plum)}
.brand-name{font:700 22px/1 "Arimo",Arial,sans-serif;color:var(--ink)}
.brand-tag{position:absolute;left:159px;top:41px;font-size:8px;font-weight:700;color:var(--ink)}
.account-links{position:absolute;right:127px;top:13px;display:flex;gap:9px;font-size:8px;color:var(--ink)}
.perks{position:absolute;top:29px;left:491px;display:flex;gap:4px}
.perk{height:26px;border-radius:3px;color:var(--white);text-align:center;padding-top:4px;line-height:1.05}
.perk b{display:block;font-size:9.5px}
.perk small{font-size:6.5px}
.perk.ship{width:83px;background:var(--orange)}
.perk.worry{width:71px;background:var(--tan)}
.perk.nz{width:89px;background:var(--slate)}
.main-nav{position:absolute;top:63px;left:0;width:868px;height:31px;background:var(--plum)}
.nav-items{position:absolute;left:125px;top:6px;display:flex;gap:4px;list-style:none}
.nav-items li{height:19px;line-height:19px;border-radius:10px;background:var(--white);font-size:8.5px;text-align:center;color:var(--ink)}
.nav-items li.active{background:var(--yellow)}
.search{position:absolute;left:600px;top:6px;width:141px;height:19px;border-radius:10px;background:var(--white);font-size:8px;line-height:19px;padding-left:10px}
.search-go{position:absolute;right:2px;top:2px;width:15px;height:15px;border-radius:50%;background:var(--plum);color:var(--white);font-size:6px;line-height:15px;text-align:center;padding:0}
.breadcrumb{position:absolute;left:127px;top:97px;font-size:8.5px;color:var(--muted)}
.breadcrumb a{color:var(--plum);text-decoration:underline}
.page-title{position:absolute;top:127px;left:0;width:868px;text-align:center;font:700 16px/1 "Arvo",serif;letter-spacing:1px}
.intro{position:absolute;top:155px;left:128px;width:612px;font-size:7.8px;line-height:10px;text-align:center;color:var(--ink)}
.policy-case{position:absolute;left:125px;width:616px;background:var(--white);border:1px solid var(--box-line)}
.case-title{position:absolute;left:0;top:10px;height:29px;padding:0 16px 0 12px;border-radius:0 15px 15px 0;background:var(--plum);color:var(--white);font:400 13px/29px "Arvo",serif}
.policy-case p,.policy-case ul,.condition{position:absolute;left:13px;width:592px;font-size:7.8px;line-height:11.3px;color:var(--ink)}
.policy-case ul{list-style:none}
.policy-case li{position:relative;padding-left:10px}
.policy-case li::before{content:"";position:absolute;left:1px;top:4px;width:4px;height:4px;border-radius:50%;background:var(--ink)}
.condition{font-weight:700;color:var(--plum)}
.site-footer{position:absolute;top:968px;left:0;width:868px;height:232px;background:var(--plum);color:var(--white)}
.footer-badge{position:absolute;left:394px;top:8px;width:80px;height:80px;border-radius:50%;background:var(--white)}
.footer-col{position:absolute;top:98px}
.footer-col h3{font:700 10px/1 "Arvo",serif;letter-spacing:.5px;margin-bottom:11px}
.footer-col ul{list-style:none;font-size:8.5px;line-height:14px}
.newsletter{position:absolute;left:589px;top:118px;width:152px;height:19px;background:var(--white)}
.newsletter span{position:absolute;right:0;top:0;width:18px;height:19px;background:var(--yellow);color:var(--plum);font-size:7px;font-weight:700;line-height:19px;text-align:center}
.follow{position:absolute;left:589px;top:148px;font:700 10px/1 "Arvo",serif;letter-spacing:.5px}
.socials{position:absolute;left:589px;top:166px;display:flex;gap:5px}
.socials i{width:13px;height:13px;border-radius:50%;background:var(--orange)}
.copyright{position:absolute;top:199px;left:0;width:868px;text-align:center;font-size:8.5px}
.to-top{position:absolute;left:782px;top:1084px}
</style>
</head>
<body>
<div class="stripe top"></div>

<header class="site-header">
  <div class="brand"><span class="brand-dot"></span><span class="brand-name">Brindlehop</span></div>
  <div class="brand-tag">Your company slogan goes here</div>
  <nav class="account-links"><span>MY ACCOUNT</span><span>WISHLIST</span><span>MY CART</span><span>CHECKOUT</span><span>LOG IN</span></nav>
  <div class="perks">
    <div class="perk ship"><b>Free shipping</b><small>on all orders over $50</small></div>
    <div class="perk worry"><b>Worry free</b><small>Return policy</small></div>
    <div class="perk nz"><b>100% NZ owned</b><small>*Conditions Apply</small></div>
  </div>
</header>

<nav class="main-nav">
  <ul class="nav-items">
    <li class="active" style="width:53px">HOME</li>
    <li style="width:64px">TODDLERS</li>
    <li style="width:55px">GIRLS</li>
    <li style="width:52px">BOYS</li>
    <li style="width:75px">ACCESSORIES</li>
    <li style="width:66px">THEMES</li>
  </ul>
  <div class="search">Enter your search<span class="search-go">GO</span></div>
</nav>

<div class="breadcrumb">Home &nbsp;»&nbsp; <a>Return &amp; exchange policy</a></div>

<h1 class="page-title">RETURN &amp; EXCHANGE POLICY</h1>
<p class="intro">Nemo enim ipsam voluptatem quia voluptas sit aspernatur aut odit aut fugit, sed quia consequuntur magni dolores eos qui ratione voluptatem sequi nesciunt. Neque porro quisquam est, qui dolorem ipsum quia dolor sit amet, consectetur, adipisci velit, sed quia non numquam eius modi tempora incidunt ut labore et dolore magnam aliquam quaerat voluptatem. Ut enim ad minima veniam, quis nostrum exercitationem ullam corporis suscipit laboriosam, nisi ut aliquid ex ea commodi consequatur? Quis autem vel eum iure reprehenderit qui in ea voluptate velit esse quam nihil molestiae consequatur, vel illum qui dolorem eum fugiat quo voluptas nulla pariatur</p>

<section class="policy-case" style="top:214px;height:168px">
  <h2 class="case-title">CASE- 1: Damaged and Defective goods received :</h2>
  <p style="top:50px">Nemo enim ipsam voluptatem quia voluptas sit aspernatur aut odit aut fugit, sed quia consequuntur magni dolores eos qui ratione voluptatem sequi nesciunt. Neque porro quisquam est, qui dolorem ipsum quia dolor sit amet, consectetur, adipisci velit, sed quia non numquam eius modi tempora incidunt ut labore et dolore magnam aliquam quaerat voluptatem. Ut enim ad minima veniam, quis nostrum exercitationem ullam corporis suscipit laboriosam, nisi ut aliquid ex ea commodi consequatur? Quis autem vel eum iure reprehenderit qui in ea voluptate velit esse quam nihil molestiae consequatur, vel illum qui dolorem eum fugiat quo voluptas nulla pariatur</p>
  <p style="top:105px">Nemo enim ipsam voluptatem quia voluptas sit aspernatur aut odit aut fugit, sed quia consequuntur magni dolores eos qui ratione voluptatem sequi nesciunt. Neque porro quisquam est, qui dolorem ipsum quia dolor sit amet, consectetur, adipisci velit, sed quia non numquam eius modi tempora incidunt ut labore et dolore magnam aliquam quaerat voluptatem. Ut enim ad minima veniam, quis nostrum exercitationem ullam corporis suscipit laboriosam, nisi ut aliquid ex ea commodi consequatur? Quis autem vel eum iure reprehenderit qui in ea voluptate velit esse quam nihil molestiae consequatur, vel illum qui dolorem eum fugiat quo voluptas nulla pariatur</p>
</section>

<section class="policy-case" style="top:394px;height:187px">
  <h2 class="case-title">CASE- 2: Product being not liked due to color variation :</h2>
  <p style="top:50px">Nemo enim ipsam voluptatem quia voluptas sit aspernatur aut odit aut fugit, sed quia consequuntur magni dolores eos qui ratione voluptatem sequi nesciunt. Neque porro quisquam est, qui dolorem ipsum quia dolor sit amet, consectetur, adipisci velit, sed quia non numquam eius modi tempora incidunt ut labore et dolore magnam aliquam quaerat voluptatem. Ut enim ad minima veniam, quis nostrum exercitationem ullam corporis suscipit laboriosam, nisi ut aliquid ex ea commodi consequatur? Quis autem vel eum iure reprehenderit qui in ea voluptate velit esse quam nihil molestiae consequatur, vel illum qui dolorem eum fugiat quo voluptas nulla pariatur</p>
  <ul style="top:105px">
    <li>If the variation is higher than expected (then norm) return is accepted.</li>
    <li>A complaint has to be made within 48 hours of receiving the goods.</li>
    <li>Complain has to be made on email with subject as "Complaint" for {Order number} and {Product code}.</li>
    <li>A picture of the product has to be sent.</li>
    <li>Our team reviews it within 1 business day and offers you a solution as a) Replace defective good immediately free of charge or. b) Offer you a credit note or. c) Refund full amount instantly.</li>
  </ul>
</section>

<section class="policy-case" style="top:594px;height:174px">
  <h2 class="case-title" style="padding-right:72px">CASE 3: Product being not liked :</h2>
  <div class="condition" style="top:51px">Condition 1</div>
  <ul style="top:65px"><li>Nemo enim ipsam voluptatem quia voluptas sit aspernatur aut odit aut fugit, sed quia consequuntur magni dolores eos qui ratione voluptatem sequi nesciunt. Neque porro quisquam est, qui dolorem ipsum quia dolor sit amet, consectetur, adipisci velit, sed quia non numquam eius modi tempora incidunt ut labore et dolore magnam aliquam quaerat voluptatem.</li></ul>
  <div class="condition" style="top:107px">Condition 2</div>
  <ul style="top:122px"><li>Nemo enim ipsam voluptatem quia voluptas sit aspernatur aut odit aut fugit, sed quia consequuntur magni dolores eos qui ratione voluptatem sequi nesciunt. Neque porro quisquam est, qui dolorem ipsum quia dolor sit amet, consectetur, adipisci velit, sed quia non numquam eius modi tempora incidunt ut labore et dolore magnam aliquam quaerat voluptatem.</li></ul>
</section>

<section class="policy-case" style="top:781px;height:168px">
  <h2 class="case-title">CASE 4: Product customized but fitting not perfect :</h2>
  <p style="top:54px">Nemo enim ipsam voluptatem quia voluptas sit aspernatur aut odit aut fugit, sed quia consequuntur magni dolores eos qui ratione voluptatem sequi nesciunt. Neque porro quisquam est, qui dolorem ipsum quia dolor sit amet, consectetur, adipisci velit, sed quia non numquam eius modi tempora incidunt ut labore et dolore magnam aliquam quaerat voluptatem. Ut enim ad minima veniam, quis nostrum exercitationem ullam corporis suscipit laboriosam, nisi ut aliquid ex ea commodi consequatur? Quis autem vel eum iure reprehenderit qui in ea voluptate velit esse quam nihil molestiae consequatur, vel illum qui dolorem eum fugiat quo voluptas nulla pariatur</p>
  <p style="top:109px">Nemo enim ipsam voluptatem quia voluptas sit aspernatur aut odit aut fugit, sed quia consequuntur magni dolores eos qui ratione voluptatem sequi nesciunt. Neque porro quisquam est, qui dolorem ipsum quia dolor sit amet, consectetur, adipisci velit, sed quia non numquam eius modi tempora incidunt ut labore et dolore magnam aliquam quaerat voluptatem. Ut enim ad minima veniam, quis nostrum exercitationem ullam corporis suscipit laboriosam, nisi ut aliquid ex ea commodi consequatur? Quis autem vel eum iure reprehenderit qui in ea voluptate velit esse quam nihil molestiae consequatur, vel illum qui dolorem eum fugiat quo voluptas nulla pariatur</p>
</section>

<footer class="site-footer">
  <div class="footer-badge"></div>
  <div class="footer-col" style="left:125px"><h3>BRINDLEHOP</h3>
    <ul><li>About Us</li><li>Contact Us</li><li>Advanced Search</li><li>Terms &amp; Conditions</li><li>Sitemap</li></ul></div>
  <div class="footer-col" style="left:278px"><h3>CUSTOMER SERVICE</h3>
    <ul><li>Shipping &amp; Delivery</li><li>Returns Policy</li><li>Sizing Guide</li><li>Contact Us</li></ul></div>
  <div class="footer-col" style="left:453px"><h3>MY ACCOUNT</h3>
    <ul><li>My Account</li><li>Order History</li><li>Wish List</li><li>Compare</li></ul></div>
  <div class="footer-col" style="left:589px"><h3>OUR NEWSLETTER</h3></div>
  <div class="newsletter"><span>GO</span></div>
  <div class="follow">FOLLOW US ON</div>
  <div class="socials"><i></i><i></i><i></i><i></i><i></i></div>
  <div class="copyright">© 2012 Brindlehop Store. All Rights Reserved.</div>
</footer>

<svg class="to-top" width="46" height="46" viewBox="0 0 46 46" aria-label="Back to top">
  <circle cx="23" cy="23" r="22" fill="var(--alert)"/>
  <path d="M23 31V16M18 21l5-5 5 5" stroke="#fff" stroke-width="2" fill="none" stroke-linecap="round"/>
</svg>

<div class="stripe bottom"></div>
</body>
</html>
```